I need a website, primarily a landing page, for my company, Harlow Ridge. A sales training and cons

I need a web design/landing page for a new sales training and consulting company, harlow ridge. We perform "sales experiments" aimed at each individual or team, where we assist in helping them identify their strengths, through a series of "sales experiments" that we can tailor based on the individual and what they're trying to accomplish.

```html
<!DOCTYPE html>
<html lang="en">
<head>
<meta charset="utf-8">
<title>Harlow Ridge — Sales Training &amp; Consulting</title>
<link rel="stylesheet" href="https://fonts.googleapis.com/css2?family=Lato:wght@400;700&family=Poppins:wght@400;500;600&display=swap">
<style>
:root{
  --blue:#2f6ea5;
  --blue-dark:#245a88;
  --ink:#1f1f1f;
  --text:#444;
  --muted:#777;
  --line:#e6e6e6;
  --paper:#fff;
  --soft:#f7f7f7;
  --dark:#262626;
  --sky:#9fd0f5;
}
*{box-sizing:border-box;margin:0;padding:0}
html,body{width:1200px;height:4500px;overflow:hidden;background:var(--paper)}
body{font-family:'Lato',sans-serif;color:var(--text);position:relative}
.abs{position:absolute}
h1,h2,h3,h4{font-family:'Poppins',sans-serif;color:var(--ink);font-weight:500}

/* top bar */
.topbar{left:138px;top:9px;width:924px;height:27px;background:var(--blue);color:#fff;font-size:11px;display:flex;align-items:center;padding:0 30px;gap:22px}
.topbar .right{margin-left:auto;display:flex;gap:10px;align-items:center}
.topbar .dot{width:9px;height:9px;border-radius:50%;background:#fff;opacity:.85}
/* nav */
.nav{left:138px;top:45px;width:924px;height:54px;display:flex;align-items:center;padding:0 150px}
.brand{display:flex;align-items:center;gap:8px;font-family:'Lato',sans-serif;font-weight:700;font-size:14px;color:var(--blue)}
.brand .mark{width:18px;height:18px;border-radius:50%;background:var(--blue)}
.menu{margin-left:auto;display:flex;gap:20px;font-size:11px;font-weight:700;color:#333;text-transform:uppercase}
.menu .on{color:var(--blue)}
/* hero */
.hero{left:138px;top:108px;width:924px;height:507px;background:linear-gradient(135deg,#3a3632 0%,#6b5b4e 35%,#a79a8c 60%,#3d3a38 100%)}
.hero-copy{left:420px;top:300px;width:300px;height:200px;background:rgba(20,30,40,.45);text-align:center;padding-top:38px}
.hero-copy .l1{font-family:'Lato',sans-serif;font-size:34px;color:var(--sky)}
.hero-copy .l2{display:inline-block;font-size:34px;color:#fff;background:rgba(47,110,165,.55);padding:0 10px;margin-top:2px}
.hero-copy .btn{display:inline-block;margin-top:14px;font-size:12px;color:#fff;border:1px solid #fff;padding:4px 14px;border-radius:3px}
.hero-copy .down{width:26px;height:26px;border:2px solid #fff;border-radius:50%;margin:8px auto 0}
/* intro */
.intro{left:195px;top:632px;font-family:'Lato',sans-serif;font-size:33px;line-height:46px;color:#555;font-weight:400}
.rule{height:3px;width:52px;background:var(--blue)}
.feature{top:760px;width:270px}
.feature svg{display:block;height:110px}
.feature h4{font-family:'Lato',sans-serif;font-weight:700;font-size:17px;margin:16px 0 10px}
.feature p{font-size:13px;line-height:22px;color:#333}
/* why */
.why-photo{left:138px;top:1100px;width:462px;height:550px;background:linear-gradient(160deg,#4a4a4a,#2c2c2c 60%,#3b3b3b)}
.why-copy{left:156px;top:1225px;color:#fff}
.why-copy h2{color:#fff;font-family:'Lato',sans-serif;font-weight:700;font-size:38px;line-height:44px}
.why-copy p{font-size:14px;margin-top:34px}
.btn-blue{display:inline-block;background:var(--blue);color:#fff;font-size:12px;font-weight:700;text-transform:uppercase;padding:12px 22px}
.why-panel{left:600px;top:1100px;width:462px;height:550px;background:var(--blue);padding:80px 0 0 72px}
.why-item{display:flex;gap:30px;margin-bottom:60px;color:#fff}
.why-item h4{color:#fff;font-family:'Lato',sans-serif;font-weight:700;font-size:20px;margin-bottom:8px}
.why-item p{font-size:13px;line-height:21px;width:300px}
/* experiments */
.exp-copy{left:192px;top:1725px;width:240px}
.exp-copy h2{font-family:'Poppins',sans-serif;font-weight:600;font-size:36px;line-height:46px}
.exp-copy p{font-size:13px;line-height:23px;color:#555;margin:30px 0 30px;width:150px}
.exp-photo{top:1734px;width:276px;height:276px}
.exp-arrow{left:1030px;top:1850px;width:20px;height:40px}
/* section titles */
.title{left:0;width:1200px;text-align:center;font-family:'Poppins',sans-serif;font-weight:600;font-size:34px;color:var(--ink)}
.title + .rule{left:574px}
/* team */
.member{top:2345px;width:270px;text-align:center}
.avatar{width:165px;height:165px;border-radius:50%;margin:0 auto;border:4px solid #eee}
.member h4{font-size:17px;font-weight:600;margin-top:22px}
.member .role{color:var(--blue);font-size:11px;margin-top:6px}
.member p{font-size:12px;line-height:22px;color:#333;margin-top:18px}
/* reviews */
.review{top:2880px;height:264px;border:1px solid var(--line);padding:40px 40px 0 45px;box-shadow:0 2px 6px rgba(0,0,0,.05)}
.review p{font-size:17px;line-height:27px;color:#555}
.review .who{margin-top:26px;display:flex;gap:12px;align-items:flex-start}
.review .who span.bar{width:24px;height:2px;background:#333;margin-top:10px}
.review .who b{display:block;font-size:13px;color:#222}
.review .who i{font-style:normal;font-size:11px;color:#888}
.review .q{position:absolute;right:40px;bottom:14px;font-size:90px;line-height:90px;color:#e3e3e3;font-family:'Poppins',sans-serif}
.dots{left:564px;top:3186px;display:flex;gap:10px}
.dots span{width:11px;height:11px;border-radius:50%;background:#ddd}
.dots span.on{background:var(--blue)}
/* blog */
.post{top:3366px;width:282px}
.post .img{height:184px;background:linear-gradient(150deg,#5d5146,#2f2a27 55%,#7a6b5c);position:relative}
.post .date{position:absolute;left:0;bottom:0;width:100%;height:30px;background:var(--blue);color:#fff;font-size:12px;font-weight:700;padding:8px 10px}
.post h4{font-family:'Poppins',sans-serif;font-weight:600;font-size:20px;margin:26px 0 14px}
.post p{font-size:13px;line-height:22px;color:#666}
.post .more{margin-top:16px;font-size:13px;font-weight:700;color:#222}
/* consultation */
.consult{left:138px;top:3918px;width:924px;height:420px;background:linear-gradient(120deg,#2e2e2e,#1d1d1d 55%,#3a3a3a)}
.consult-copy{left:190px;top:3995px;width:395px;text-align:right;color:#fff}
.consult-copy h2{color:#fff;font-family:'Poppins',sans-serif;font-weight:500;font-size:36px;line-height:44px}
.consult-copy p{font-size:14px;line-height:24px;margin-top:30px;color:#ddd;text-align:center}
.field{background:#fff;font-size:13px;color:#888;padding:12px 16px}
.send{left:612px;top:4212px;background:var(--blue);color:#fff;font-size:12px;font-weight:700;text-transform:uppercase;padding:12px 14px}
/* call bar */
.callbar{left:138px;top:4338px;width:924px;height:102px;background:var(--blue);display:flex;align-items:center;padding:0 20px;color:#fff}
.callbar h3{color:#fff;font-family:'Poppins',sans-serif;font-weight:500;font-size:27px}
.callbar .phone{margin-left:auto;background:#1b1b1b;color:#fff;font-size:14px;font-weight:700;padding:14px 24px}
/* footer */
.footer{left:138px;top:4455px;width:924px;height:40px;display:flex;align-items:center;font-size:11px;color:#444}
.footer .copy{margin-left:255px}
.footer .copy a{color:var(--blue);text-decoration:none}
</style>
</head>
<body>

<div class="abs topbar">
  <span>⌂ 14 Ridge Lane, Suite 3</span>
  <span>✉ hello@harlowridge.example</span>
  <div class="right"><span>Call Us +1 555 014 2380</span><span class="dot"></span><span class="dot"></span><span class="dot"></span><span class="dot"></span></div>
</div>

<header class="abs nav">
  <div class="brand"><span class="mark"></span>Harlow Ridge</div>
  <nav class="menu"><span class="on">Home</span><span>Experiments</span><span>Our Team</span><span>About</span><span>Services</span><span>Blog</span><span>Contact Us</span></nav>
</header>

<section class="abs hero" role="img" aria-label="Photo of a smiling business team gathered around a laptop in an office"></section>
<div class="abs hero-copy">
  <div class="l1">Success</div>
  <div class="l2">Is in your DNA</div><br>
  <span class="btn">Find with Us</span>
  <div class="down"><svg width="22" height="22" viewBox="0 0 22 22"><path d="M6 8l5 5 5-5" stroke="#fff" stroke-width="2" fill="none"/></svg></div>
</div>

<h2 class="abs intro">We Help you to gain insight into your life<br>and into your business.</h2>
<div class="abs rule" style="left:195px;top:735px"></div>

<div class="abs feature" style="left:195px">
  <svg viewBox="0 0 110 110" width="110"><path d="M30 12h50v22c0 18-11 30-25 30S30 52 30 34z" fill="var(--blue)"/><path d="M30 18H14c0 16 8 24 18 26M80 18h16c0 16-8 24-18 26" stroke="var(--blue)" stroke-width="6" fill="none"/><rect x="50" y="62" width="10" height="18" fill="var(--blue)"/><rect x="36" y="80" width="38" height="10" fill="var(--blue)"/></svg>
  <h4>Expert In Sales</h4>
  <p>Lorem ipsum dolor sit amet, consectetur adipiscing elit. Suspendisse nec turpis posuere, facilisis mauris sed, ornare eros. Class aptent taciti sociosqu ad litora torquent per conubia nostra, per inceptos himenaeos.</p>
</div>
<div class="abs feature" style="left:468px">
  <svg viewBox="0 0 110 110" width="110"><circle cx="55" cy="55" r="50" fill="var(--blue)"/><circle cx="55" cy="55" r="38" fill="#fff"/><circle cx="55" cy="55" r="28" fill="var(--blue)"/><circle cx="55" cy="55" r="17" fill="#fff"/><circle cx="55" cy="55" r="8" fill="var(--blue)"/></svg>
  <h4>Qualified Trainers</h4>
  <p>Lorem ipsum dolor sit amet, consectetur adipiscing elit. Suspendisse nec turpis posuere, facilisis mauris sed, ornare eros. Class aptent taciti sociosqu ad litora torquent per conubia nostra, per inceptos himenaeos.</p>
</div>
<div class="abs feature" style="left:744px">
  <svg viewBox="0 0 110 110" width="110"><rect x="6" y="20" width="80" height="80" fill="none" stroke="var(--blue)" stroke-width="7"/><path d="M22 52l24 24 58-66" stroke="var(--blue)" stroke-width="13" fill="none"/></svg>
  <h4>Long Term Experience</h4>
  <p>Lorem ipsum dolor sit amet, consectetur adipiscing elit. Suspendisse nec turpis posuere, facilisis mauris sed, ornare eros. Class aptent taciti sociosqu ad litora torquent per conubia nostra, per inceptos himenaeos.</p>
</div>

<section class="abs why-photo" role="img" aria-label="Dim photo of a sales meeting in progress"></section>
<div class="abs why-copy">
  <h2>Why<br>Choose Us</h2>
  <p>You will not regret to Choos US</p>
  <span class="btn-blue" style="margin-top:26px">Learn More</span>
</div>
<div class="abs why-panel">
  <div class="why-item">
    <svg width="44" height="44" viewBox="0 0 44 44"><circle cx="22" cy="14" r="10" fill="none" stroke="#fff" stroke-width="3"/><path d="M4 42c0-10 8-16 18-16s18 6 18 16" fill="none" stroke="#fff" stroke-width="3"/></svg>
    <div><h4>Lorem Ipsum</h4><p>Lorem ipsum dolor sit amet, dolor pt.Percipit imper feruto nulla nosumo amet dolo.</p></div>
  </div>
  <div class="why-item">
    <svg width="44" height="44" viewBox="0 0 44 44"><path d="M2 22C2 10 12 4 22 4s20 6 20 18z" fill="none" stroke="#fff" stroke-width="3"/><path d="M22 22v14c0 4-6 4-6 0" fill="none" stroke="#fff" stroke-width="3"/></svg>
    <div><h4>Lorem Ipsum</h4><p>Lorem ipsum dolor sit amet, dolor pt.Percipit imper feruto nulla nosumo amet dolo.</p></div>
  </div>
  <div class="why-item">
    <svg width="44" height="44" viewBox="0 0 44 44"><circle cx="22" cy="22" r="19" fill="none" stroke="#fff" stroke-width="3"/><text x="22" y="30" text-anchor="middle" fill="#fff" font-family="Lato,sans-serif" font-weight="700" font-size="22">$</text></svg>
    <div><h4>Lorem Ipsum</h4><p>Lorem ipsum dolor sit amet, dolor pt.Percipit imper feruto nulla nosumo amet dolo.</p></div>
  </div>
</div>

<div class="abs exp-copy">
  <h2>Recent<br>Experiments</h2>
  <p>Lorem IpsumLorem IpsumLorem IpsumLorem IpsumLorem Ipsum</p>
  <span class="btn-blue">Go to work</span>
</div>
<div class="abs exp-photo" style="left:456px;background:linear-gradient(160deg,#6a6a66,#3a3835 50%,#8b8880)" role="img" aria-label="Photo of a trainer presenting to a seated group"></div>
<div class="abs exp-photo" style="left:756px;background:linear-gradient(140deg,#8a8d92,#4d5560 50%,#b7b4ae)" role="img" aria-label="Photo of hands working at a laptop with documents"></div>
<svg class="abs exp-arrow" viewBox="0 0 20 40"><path d="M4 6l12 14-12 14" stroke="#fff" stroke-width="3" fill="none"/></svg>

<div class="abs" style="left:138px;top:2160px;width:924px;height:1px;background:var(--line)"></div>
<h2 class="abs title" style="top:2192px">Our Team</h2>
<div class="abs rule" style="top:2250px;left:574px"></div>
<p class="abs" style="left:0;width:1200px;top:2270px;text-align:center;font-size:11px;color:#333">Thay will hold your Hand to Success</p>

<div class="abs member" style="left:189px">
  <div class="avatar" style="background:radial-gradient(circle at 50% 40%,#c89a7a,#7a4a30 70%)" role="img" aria-label="Portrait photo of a trainer"></div>
  <h4>Lorrum Ipsum</h4><div class="role">Your Trainer</div>
  <p>Lorrum Ipsum Lorrum IpsumLorrum<br>Lorrum Ipsum Lorrum Ipsum Lorrum</p>
</div>
<div class="abs member" style="left:480px">
  <div class="avatar" style="background:radial-gradient(circle at 50% 40%,#d9b89e,#8c6a52 70%)" role="img" aria-label="Portrait photo of a trainer"></div>
  <h4>Lorrum Ipsum</h4><div class="role">Your Trainer</div>
  <p>Lorrum Ipsum Lorrum IpsumLorrum<br>Lorrum Ipsum Lorrum Ipsum Lorrum</p>
</div>
<div class="abs member" style="left:735px">
  <div class="avatar" style="background:radial-gradient(circle at 50% 40%,#c89a7a,#7a4a30 70%)" role="img" aria-label="Portrait photo of a trainer"></div>
  <h4>Lorrum Ipsum</h4><div class="role">Your Trainer</div>
  <p>Lorrum Ipsum Lorrum IpsumLorrum<br>Lorrum Ipsum Lorrum Ipsum Lorrum</p>
</div>

<div class="abs" style="left:138px;top:2720px;width:924px;height:1px;background:var(--line)"></div>
<h2 class="abs title" style="top:2755px">Reviews &amp; Testimonials</h2>
<div class="abs rule" style="top:2812px;left:574px"></div>

<div class="abs review" style="left:156px;width:438px">
  <p>Sed et justo eget metus commodo facilisis. Duis at laoreet nulla. Curabitur ut libero bibendum nulla tristique interdum non posuere ligula.</p>
  <div class="who"><span class="bar"></span><div><b>Lorem Ipsum</b><i>CEO Lorem Ipsum</i></div></div>
  <span class="q">”</span>
</div>
<div class="abs review" style="left:621px;width:423px">
  <p>Sed et justo eget metus commodo facilisis. Duis at laoreet nulla. Curabitur ut libero bibendum nulla tristique interdum non posuere ligula.</p>
  <div class="who"><span class="bar"></span><div><b>Lorem Ipsum</b><i>CEO Lorem Ipsum</i></div></div>
  <span class="q">”</span>
</div>
<div class="abs dots"><span></span><span class="on"></span><span></span><span></span></div>

<h2 class="abs title" style="top:3245px">Latest From Our Blog</h2>
<div class="abs rule" style="top:3302px;left:574px"></div>

<article class="abs post" style="left:153px">
  <div class="img" role="img" aria-label="Photo of a person reviewing paperwork at a desk"><span class="date">23 OCTOBER, 2018</span></div>
  <h4>Lorem Ipsum</h4>
  <p>Lorem ipsum dolor sit amet, consectetur adipiscing elit. Suspendisse nec turpis posuere, facilisis mauris sed, ornare eros. Class aptent taciti sociosqu ad litora torquent per conubia nostra, per inceptos himenaeos. Maecenas</p>
  <div class="more">Learn More →</div>
</article>
<article class="abs post" style="left:459px">
  <div class="img" role="img" aria-label="Photo of a person reviewing paperwork at a desk"><span class="date">23 OCTOBER, 2018</span></div>
  <h4>Lorem Ipsum</h4>
  <p>Lorem ipsum dolor sit amet, consectetur adipiscing elit. Suspendisse nec turpis posuere, facilisis mauris sed, ornare eros. Class aptent taciti sociosqu ad litora torquent per conubia nostra, per inceptos himenaeos. Maecenas</p>
  <div class="more">Learn More →</div>
</article>
<article class="abs post" style="left:765px">
  <div class="img" role="img" aria-label="Photo of a person reviewing paperwork at a desk"><span class="date">23 OCTOBER, 2018</span></div>
  <h4>Lorem Ipsum</h4>
  <p>Lorem ipsum dolor sit amet, consectetur adipiscing elit. Suspendisse nec turpis posuere, facilisis mauris sed, ornare eros. Class aptent taciti sociosqu ad litora torquent per conubia nostra, per inceptos himenaeos. Maecenas</p>
  <div class="more">Learn More →</div>
</article>

<section class="abs consult" role="img" aria-label="Dark photo of an office workspace behind the consultation form"></section>
<div class="abs consult-copy">
  <h2>Request<br>A Free Consultation</h2>
  <p>Lorrum Ipsum Lorrum IpsumLorrum IpsumLorrum<br>IpsumLorrum IpsumLorrum IpsumLorrum Ipsum</p>
</div>
<div class="abs field" style="left:612px;top:4020px;width:210px;height:45px">Your Name*</div>
<div class="abs field" style="left:843px;top:4020px;width:201px;height:45px">Your Email*</div>
<div class="abs field" style="left:612px;top:4080px;width:432px;height:114px">Your Message*</div>
<div class="abs send">Send Request</div>

<div class="abs callbar">
  <h3>Wish To Make A Quick Contact..? Just Make A Call</h3>
  <span class="phone">+1 555 014 2387</span>
</div>

<footer class="abs footer">
  <div class="brand" style="font-size:11px"><span class="mark" style="width:12px;height:12px"></span>Harlow Ridge</div>
  <div class="copy">Copyright © 2018 Harlow Ridge. Use of this website constitutes acceptance of our <a>User Agreement</a> and <a>Privacy Policy</a>.</div>
</footer>

</body>
</html>
```